Tarrow Consulting Needs Standardised Stationery!

Hello,I am looking at having some standardised stationery to continue building my brand. I am looking for a relatively clean and simple designs using the colours from my logos. Tarrow Consulting is the main business with Quillmere Careers Australia a subsidiary.
In particular I am after a design for:
- Letterhead (very important), white background, professional, corporate that I can send to prospective clients. Logo colours.
- Envelope, standard design I can print onto envelopes.
- Pens
- Other stationery/promotional items I can create

Target Market(s)

Universities, government, large organisations.

Industry/Entity Type

Professional Service

Font styles to use
Serif

Requirements
Must have
• Logo, match the design of the Tarrow Consulting logo. Black Quillmere Careers Australia logo is a subsidiary.
Should not have
• Too much colour, some colour is good, but I am looking for a clean professional look.

```html
<!DOCTYPE html>
<html lang="en">
<head>
<meta charset="utf-8">
<title>Tarrow Consulting — Business Card</title>
<link rel="stylesheet" href="https://fonts.googleapis.com/css2?family=Lato:wght@400;700&family=Merriweather:wght@700&family=Montserrat:wght@400;500&family=Open+Sans:wght@400&display=swap">
<style>
  :root {
    --backdrop: #5a5a5a;
    --card-light: #ffffff;
    --card-dark: #232528;
    --ink: #1e1e1e;
    --ink-soft: #3a3a3a;
    --ink-light: #e4e4e4;
    --brand-blue: #2a8fcf;
    --brand-green: #22a74f;
    --brand-orange: #e8862a;
    --rule-dark: #34373b;
  }
  * { margin: 0; padding: 0; box-sizing: border-box; }
  html, body { width: 1200px; height: 802px; overflow: hidden; }
  body { background: var(--backdrop); position: relative; font-family: "Lato", sans-serif; }

  .card {
    position: absolute; top: 274px; width: 443px; height: 265px;
    box-shadow: 3px 4px 8px rgba(0,0,0,0.45);
  }
  .card--front { left: 136px; background: var(--card-light); }
  .card--back { left: 624px; background: var(--card-dark); }

  /* Wordmark */
  .wordmark { position: absolute; display: flex; align-items: center; }
  .wordmark__square { flex: none; background: var(--ink); }
  .wordmark__text { font-family: "Montserrat", sans-serif; font-weight: 500; color: var(--ink); line-height: 1; white-space: nowrap; }
  .wordmark__name { display: block; }
  .wordmark__tag { display: block; font-weight: 400; }

  .card--front .wordmark { left: 32px; top: 112px; gap: 11px; }
  .card--front .wordmark__square { width: 42px; height: 42px; }
  .card--front .wordmark__name { font-size: 22px; letter-spacing: 0.6px; }
  .card--front .wordmark__tag { font-size: 8px; letter-spacing: 6.2px; margin-top: 2px; }

  .card--back .wordmark { left: 99px; top: 102px; gap: 15px; }
  .card--back .wordmark__square { width: 61px; height: 61px; background: var(--ink-light); }
  .card--back .wordmark__text { color: var(--ink-light); }
  .card--back .wordmark__name { font-size: 31px; letter-spacing: 1px; }
  .card--back .wordmark__tag { font-size: 11px; letter-spacing: 9.2px; margin-top: 4px; }

  /* Divider */
  .divider { position: absolute; left: 228px; top: 66px; width: 2px; height: 132px;
    background: linear-gradient(var(--brand-blue) 0 33%, var(--brand-green) 33% 66%, var(--brand-orange) 66% 100%); }

  /* Contact block */
  .contact { position: absolute; left: 246px; top: 63px; color: var(--ink-soft); }
  .contact__name { font-family: "Lato", sans-serif; font-weight: 700; font-size: 16.5px; color: var(--ink); line-height: 1.1; }
  .contact__role { font-family: "Open Sans", sans-serif; font-size: 12px; line-height: 1.2; margin-bottom: 5px; }
  .contact__list { list-style: none; font-family: "Open Sans", sans-serif; font-size: 12.2px; line-height: 15.7px; }
  .contact__list li { display: flex; align-items: center; gap: 4px; }
  .contact__list svg { width: 10px; height: 10px; fill: var(--ink); flex: none; }
  .contact__address { font-family: "Open Sans", sans-serif; font-size: 12.8px; line-height: 15.5px; margin-top: 5px; }

  /* Back card */
  .rule { position: absolute; left: 46px; right: 46px; top: 195px; height: 1px; background: var(--rule-dark); }
  .subsidiary { position: absolute; left: 152px; top: 205px; display: flex; align-items: center; gap: 6px; color: var(--ink-light); }
  .subsidiary__circle { width: 33px; height: 33px; border-radius: 50%; background: var(--ink-light); flex: none; }
  .subsidiary__name { font-family: "Merriweather", serif; font-weight: 700; font-size: 13.5px; line-height: 1.1; white-space: nowrap; }
  .subsidiary__place { font-family: "Merriweather", serif; font-weight: 700; font-size: 7.5px; display: block; margin-top: 1px; }
</style>
</head>
<body>

<section class="card card--front" aria-label="Business card front">
  <div class="wordmark">
    <span class="wordmark__square"></span>
    <span class="wordmark__text">
      <span class="wordmark__name">TARROW</span>
      <span class="wordmark__tag">CONSULTING</span>
    </span>
  </div>

  <div class="divider"></div>

  <div class="contact">
    <p class="contact__name">DANIEL HARTLEY</p>
    <p class="contact__role">Managing Director</p>
    <ul class="contact__list">
      <li><svg viewBox="0 0 10 10"><path d="M1 3.5C1 2 3 1.5 5 1.5S9 2 9 3.5V4.5H7V3.5H3V4.5H1Z M2 5H8L9 9H1Z"/></svg>044-987 654 321</li>
      <li><svg viewBox="0 0 10 10"><path d="M3 0.5H7A1 1 0 0 1 8 1.5V8.5A1 1 0 0 1 7 9.5H3A1 1 0 0 1 2 8.5V1.5A1 1 0 0 1 3 0.5ZM3.2 1.8V7.6H6.8V1.8Z"/></svg>044-987 654 321</li>
      <li><svg viewBox="0 0 10 10"><path d="M0.5 2H9.5V8H0.5ZM1.5 3V3.4L5 5.6L8.5 3.4V3L5 5.1Z"/></svg>info@tarrowconsulting.com</li>
      <li><svg viewBox="0 0 10 10"><circle cx="5" cy="5" r="4.5"/></svg>www.tarrowconsulting.com</li>
    </ul>
    <p class="contact__address">27 Fernbrook Lane<br>Oakridge Vale, 4821.</p>
  </div>
</section>

<section class="card card--back" aria-label="Business card back">
  <div class="wordmark">
    <span class="wordmark__square"></span>
    <span class="wordmark__text">
      <span class="wordmark__name">TARROW</span>
      <span class="wordmark__tag">CONSULTING</span>
    </span>
  </div>

  <div class="rule"></div>

  <div class="subsidiary">
    <span class="subsidiary__circle"></span>
    <span class="subsidiary__name">Quillmere Careers<span class="subsidiary__place">Australia</span></span>
  </div>
</section>

</body>
</html>
```